Tavenne Gymnastics needs a home page collage design

Tavenne Gymnastics is creating a new website and we need a new collage for home page. Collage should combine three attached pictures of rhythmic gymnasts to create modern and feminine home page.Our colors are navy blue and white with additional colors of purple, lilac and/or light turquoise blue. Would love to see either something with smoke dispersion effect or swirls like the other two pictures attached.

Target Market(s)

parents and children ages 3 to 18

Font styles to use
Other font styles liked:
• pristina

Colors
b7cde4
886aae
85cae6
ffffff

Requirements
Must have
• sleek modern feminine look with photos provided

```html
<!DOCTYPE html>
<html lang="en">
<head>
<meta charset="utf-8">
<title>Tavenne Gymnastics — Home</title>
<link rel="stylesheet" href="https://fonts.googleapis.com/css2?family=Oswald:wght@200;400;500&family=Montserrat:wght@400;500&display=swap">
<style>
  :root {
    --navy: #0f2a78;
    --navy-dark: #0b1f63;
    --sky-light: #b4e2fc;
    --sky-mid: #6cbcf9;
    --sky-deep: #0a82fd;
    --white: #ffffff;
    --text-grey: #5a6478;
    --divider: #c8d4ea;
    --photo-top: #cfe6f6;
    --photo-bottom: #d9cdbf;
  }
  * { margin: 0; padding: 0; box-sizing: border-box; }
  html, body { width: 1200px; height: 1072px; overflow: hidden; background: var(--white); }
  body { position: relative; font-family: "Montserrat", sans-serif; color: var(--navy); }

  .hero {
    position: absolute; left: 0; top: 0; width: 1200px; height: 899px;
    background:
      radial-gradient(ellipse 620px 520px at 380px 250px, rgba(190,232,255,0.95), rgba(190,232,255,0) 70%),
      linear-gradient(100deg, var(--sky-light) 0%, #8fd0fb 40%, var(--sky-mid) 65%, var(--sky-deep) 100%);
  }

  .brand { position: absolute; left: 45px; top: 54px; display: flex; align-items: center; gap: 10px; }
  .brand-mark { width: 13px; height: 13px; border-radius: 50%; background: var(--navy); }
  .brand-name { font-family: "Montserrat", sans-serif; font-weight: 500; font-size: 25px; color: var(--navy); }
  .brand-tagline { position: absolute; left: 173px; top: 103px; font-size: 11px; color: var(--navy); }

  .main-nav { position: absolute; top: 58px; left: 0; width: 1200px; height: 24px; }
  .main-nav a {
    position: absolute; top: 0; font-family: "Oswald", sans-serif; font-weight: 400;
    font-size: 15px; color: var(--white); text-decoration: none; text-transform: uppercase; white-space: nowrap;
  }
  .main-nav a.is-active { color: var(--navy); }
  .nav-marker { position: absolute; left: 419px; top: 83px; width: 3px; height: 19px; background: var(--navy); }

  .slide-photo {
    position: absolute; left: 230px; top: 150px; width: 430px; height: 530px;
    background: linear-gradient(180deg, var(--photo-top) 0%, var(--photo-bottom) 100%);
    opacity: 0.75;
  }

  .slide-frame {
    position: absolute; left: 224px; top: 221px; width: 552px; height: 465px;
    border: 6px solid var(--white); border-right: none;
  }
  .frame-right-top { position: absolute; left: 770px; top: 221px; width: 6px; height: 150px; background: var(--white); }
  .frame-right-bottom { position: absolute; left: 770px; top: 580px; width: 6px; height: 106px; background: var(--white); }

  .slide-title {
    position: absolute; left: 656px; top: 373px; font-family: "Oswald", sans-serif; font-weight: 200;
    font-size: 56px; line-height: 1; letter-spacing: 18px; color: var(--navy-dark);
  }
  .more-button {
    position: absolute; left: 951px; top: 387px; width: 88px; height: 31px; background: var(--navy);
    color: var(--white); font-family: "Oswald", sans-serif; font-weight: 500; font-size: 14px; letter-spacing: 1.5px;
    display: flex; align-items: center; justify-content: center; gap: 6px;
  }
  .slide-text {
    position: absolute; left: 629px; top: 435px; width: 410px; height: 137px; background: var(--white);
    padding: 20px 30px; font-size: 12.2px; line-height: 19.5px; color: var(--navy-dark); overflow: hidden;
  }
  .slide-counter { position: absolute; left: 712px; top: 625px; font-family: "Oswald", sans-serif; color: var(--white); }
  .slide-counter .current { font-size: 26px; font-weight: 500; }
  .slide-counter .sep { font-size: 24px; font-weight: 200; margin: 0 2px; }
  .slide-counter .total { font-size: 15px; font-weight: 400; opacity: 0.7; }

  .learn-more { position: absolute; left: 224px; top: 704px; display: flex; align-items: center; gap: 8px; }
  .learn-more .rule { width: 35px; height: 3px; background: var(--white); }
  .learn-more span { font-family: "Oswald", sans-serif; font-size: 16px; color: var(--white); text-transform: uppercase; }

  .slide-arrows { position: absolute; left: 691px; top: 732px; display: flex; gap: 9px; }
  .slide-arrows svg { display: block; }

  .social { position: absolute; left: 24px; top: 811px; display: flex; align-items: center; gap: 14px; }
  .social .dot { width: 10px; height: 10px; border-radius: 50%; background: rgba(255,255,255,0.85); margin: 0 5px; }
  .social .feed { width: 30px; height: 30px; border-radius: 50%; border: 2px solid var(--white); }
  .social .rule { width: 81px; height: 2px; background: var(--white); margin-left: 2px; }

  .scroll-cue { position: absolute; left: 1119px; top: 708px; width: 20px; }
  .scroll-cue span { display: block; transform: rotate(-90deg); transform-origin: left top; position: absolute; left: 2px; top: 36px;
    font-size: 11px; color: var(--white); }
  .scroll-cue .rule { position: absolute; left: 7px; top: 44px; width: 3px; height: 60px; background: var(--white); }

  .info-card {
    position: absolute; left: 161px; top: 869px; width: 878px; height: 150px; background: var(--white);
    box-shadow: 0 6px 24px rgba(20,60,130,0.10);
  }
  .info-block { position: absolute; top: 36px; }
  .info-block h3 { font-family: "Oswald", sans-serif; font-weight: 500; font-size: 14px; letter-spacing: 2.5px; color: var(--navy); margin-bottom: 12px; }
  .info-block p { font-size: 12.2px; line-height: 19.5px; color: var(--text-grey); }
  .info-divider { position: absolute; top: 21px; width: 1px; height: 107px; background: var(--divider); }
  .badge { position: absolute; }

  .copyright { position: absolute; left: 0; top: 1037px; width: 1200px; text-align: center; font-size: 11.5px; color: var(--text-grey); }
</style>
</head>
<body>
  <section class="hero">
    <div class="slide-photo" role="img" aria-label="Photo of a rhythmic gymnast balancing a ball on her arm"></div>

    <div class="brand">
      <span class="brand-name">Tavenne Gymnastics</span>
      <span class="brand-mark"></span>
    </div>
    <div class="brand-tagline">School of Champions</div>

    <nav class="main-nav">
      <a class="is-active" style="left:405px">Home</a>
      <a style="left:463px">About</a>
      <a style="left:528px">Program</a>
      <a style="left:609px">Schedule</a>
      <a style="left:692px">Coastline Cup</a>
      <a style="left:823px">Holiday Cup</a>
      <a style="left:922px">Gallery</a>
      <a style="left:995px">Resources</a>
      <a style="left:1087px">Contact Us</a>
    </nav>
    <div class="nav-marker"></div>

    <div class="slide-frame"></div>
    <div class="frame-right-top"></div>
    <div class="frame-right-bottom"></div>

    <div class="slide-title">BALL</div>
    <div class="more-button">MORE
      <svg width="14" height="12" viewBox="0 0 14 12"><path d="M1 6h11M7 1l5 5-5 5" fill="none" stroke="#fff" stroke-width="2"/></svg>
    </div>
    <div class="slide-text">Ball is by tradition an elegant and “lyrical” rather than a dynamic apparatus. This means that a more sensuous relationship between the body and the apparatus is required. The ball moves in perfect harmony with the body. Spectacular throws with control and precision in</div>
    <div class="slide-counter"><span class="current">2</span><span class="sep">/</span><span class="total">3</span></div>

    <div class="learn-more"><div class="rule"></div><span>Learn more about ball</span></div>

    <div class="slide-arrows">
      <svg width="38" height="38" viewBox="0 0 38 38"><circle cx="19" cy="19" r="17.5" fill="none" stroke="#fff" stroke-width="2"/><path d="M26 19H12M17 14l-5 5 5 5" fill="none" stroke="#fff" stroke-width="2"/></svg>
      <svg width="38" height="38" viewBox="0 0 38 38"><circle cx="19" cy="19" r="17.5" fill="none" stroke="#fff" stroke-width="2"/><path d="M12 19h14M21 14l5 5-5 5" fill="none" stroke="#fff" stroke-width="2"/></svg>
    </div>

    <div class="social">
      <span class="dot"></span><span class="dot"></span><span class="dot"></span>
      <span class="feed"></span>
      <span class="rule"></span>
    </div>

    <div class="scroll-cue"><span>Scroll</span><div class="rule"></div></div>
  </section>

  <section class="info-card">
    <div class="info-block" style="left:30px">
      <h3>ADDRESS:</h3>
      <p>4270 Marlowe Avenue, #212<br>Westbrook, CA 91408</p>
    </div>
    <div class="info-divider" style="left:254px"></div>
    <div class="info-block" style="left:314px">
      <h3>PHONE:</h3>
      <p>818-555-0142 Office<br>818-555-0187 Head Coach<br>818-555-0163 Administrator</p>
    </div>
    <div class="info-divider" style="left:542px"></div>
    <svg class="badge" style="left:612px;top:30px" width="60" height="78" viewBox="0 0 60 78" role="img" aria-label="Member club badge"><rect x="6" y="4" width="48" height="70" rx="6" fill="#e7edf7"/></svg>
    <svg class="badge" style="left:726px;top:40px" width="100" height="48" viewBox="0 0 100 48" role="img" aria-label="Partner badge"><rect x="2" y="2" width="96" height="44" rx="6" fill="#e7edf7"/></svg>
  </section>

  <footer class="copyright">Copyright © 2019 · Tavenne Gymnastics.</footer>
</body>
</html>
```